Gaming Developer Wordpress Website

I am looking for someone to design a standout website for my video game developer website. We are currently developing a strategy / sim game.
Id like the following pages:
1) Games (will have a picture icon of games that we release, gamers can click each to take them to another page specifically about that game)
2) News (this will host news on coming soon or released games and general content updates)
3) Videos (this might host videos on my games or link to my ClipVane account)
4) Company (general about, mission, vison, and other info on the team and founder)
5) Support (a form gamers can fill out for help)
Id like the ability for gamers to create an account and sign up for my company newsletter.
At some point I want to be able to add a forum to my site to drive further traffic and allow gamers to discuss my games, so please make sure this is possible.
Design and color wise:
I would like the background to be a dark color, preferably black or maybe grey. I am looking for something clean, and that properly fits the gaming space.
(Lastly, I own the domain for my site, and it is currently hosted on wordpress).

```html
<!DOCTYPE html>
<html lang="en">
<head>
<meta charset="utf-8">
<title>Ravel — Game Studio</title>
<link rel="stylesheet" href="https://fonts.googleapis.com/css2?family=Poppins:wght@400;500;600;700;800;900&family=Rubik:wght@400;500;600&display=swap">
<style>
:root{
  --bg:#0d1116;
  --bg-2:#121820;
  --panel:#1a2029;
  --panel-2:#222a35;
  --line:#2b3440;
  --green:#45f882;
  --green-dark:#1fbf5c;
  --yellow:#ffbe18;
  --white:#ffffff;
  --muted:#8c96a3;
  --muted-2:#5f6975;
}
*{box-sizing:border-box;margin:0;padding:0}
html,body{width:1200px;height:4404px;overflow:hidden;background:var(--bg)}
body{font-family:"Rubik",sans-serif;color:var(--white)}
.canvas{position:relative;width:1200px;height:4404px;overflow:hidden;background:var(--bg)}
.abs{position:absolute}
.heading{font-family:"Poppins",sans-serif;font-weight:800;text-transform:uppercase;letter-spacing:.02em}
.eyebrow{font-family:"Poppins",sans-serif;font-size:11px;font-weight:600;letter-spacing:.25em;color:var(--green);text-transform:uppercase;text-align:center}
.sec-title{font-family:"Poppins",sans-serif;font-weight:800;font-size:27px;text-transform:uppercase;text-align:center}
.hex-btn{display:flex;align-items:center;justify-content:center;font-family:"Poppins",sans-serif;font-weight:700;font-size:13px;text-transform:uppercase;letter-spacing:.06em;color:var(--white);border:2px solid var(--green);clip-path:polygon(10% 0,90% 0,100% 50%,90% 100%,10% 100%,0 50%);background:rgba(69,248,130,.08)}
.yellow-btn{display:flex;align-items:center;justify-content:center;background:var(--yellow);color:#111;font-family:"Poppins",sans-serif;font-weight:700;font-size:10px;text-transform:uppercase;border-radius:2px}

/* Header & hero */
.hero{left:0;top:0;width:1200px;height:630px}
.hero-art{left:0;top:0;width:1200px;height:610px;background:
  radial-gradient(ellipse at 18% 45%,rgba(80,200,220,.35),transparent 45%),
  radial-gradient(ellipse at 82% 40%,rgba(200,80,200,.35),transparent 45%),
  linear-gradient(180deg,#3a2f7a 0%,#4b3a92 35%,#2b2f6a 70%,#1a1d3b 100%)}
.logo{left:193px;top:14px;display:flex;align-items:center;gap:8px;font-family:"Poppins",sans-serif;font-weight:800;font-size:22px;letter-spacing:.04em}
.logo-box{width:22px;height:22px;background:var(--white)}
.nav{left:400px;top:25px;display:flex;gap:30px;font-family:"Poppins",sans-serif;font-weight:600;font-size:12px;text-transform:uppercase}
.nav span:first-child{color:var(--green)}
.search{left:842px;top:24px}
.signin{left:865px;top:18px;width:100px;height:32px;font-size:11px}
.menu{left:980px;top:24px}
.hero-kicker{left:0;top:182px;width:1200px;text-align:center;font-family:"Poppins",sans-serif;font-weight:700;font-size:30px;letter-spacing:.28em}
.hero-title{left:0;top:218px;width:1200px;text-align:center;font-family:"Poppins",sans-serif;font-weight:900;font-size:86px;line-height:1;letter-spacing:.01em;text-shadow:0 4px 0 rgba(0,0,0,.25)}
.hero-title b{color:var(--white);-webkit-text-stroke:0}
.hero-text{left:340px;top:322px;width:520px;text-align:center;font-family:"Poppins",sans-serif;font-weight:600;font-size:14px;line-height:1.45;text-transform:uppercase}
.hero-btn{left:522px;top:405px;width:156px;height:42px}
.hero-tabs{left:0;top:552px;width:1200px;display:flex;justify-content:center;gap:90px;font-family:"Poppins",sans-serif;font-size:11px;font-weight:600;text-transform:uppercase}
.hero-tabs span{padding:4px 14px}
.hero-tabs span:first-child{border:1px solid rgba(255,255,255,.7)}
.hero-edge{left:0;top:585px}

/* NFT strip */
.nft-strip{left:0;top:630px;width:1200px;height:200px;background:var(--bg-2)}
.nft-card{top:38px;width:258px;height:122px;background:var(--panel);border:1px solid var(--line);display:flex;gap:12px;padding:10px}
.nft-thumb{width:98px;height:100px;border-radius:2px}
.nft-info{display:flex;flex-direction:column;padding-top:8px}
.nft-name{font-family:"Poppins",sans-serif;font-weight:700;font-size:12px;text-transform:uppercase}
.nft-by{display:flex;align-items:center;gap:5px;font-size:9px;color:var(--muted);margin-top:10px}
.dot-av{width:16px;height:16px;border-radius:50%;background:#b98c4a}
.nft-foot{display:flex;align-items:center;gap:10px;margin-top:28px;font-size:10px;font-weight:600}
.nft-foot .yellow-btn{width:44px;height:18px}

/* Streamers */
.streamers{left:0;top:830px;width:1200px;height:640px;background:radial-gradient(ellipse at 70% 40%,#1b232b 0%,var(--bg) 60%)}
.tab-btn{top:207px;width:100px;height:30px;font-size:10px}
.avatars{left:418px;top:273px;display:flex;gap:28px}
.avatar{width:40px;height:40px;border-radius:50%;border:2px solid var(--yellow);background:radial-gradient(circle,#6d4a8a,#2a2240)}
.avatar-line{left:274px;top:333px;width:652px;height:2px;background:var(--line)}
.avatar-line i{position:absolute;left:240px;width:170px;height:2px;background:var(--green)}
.feature{left:193px;top:375px;width:812px;height:222px;background:var(--panel);border:1px solid var(--line)}
.feature-art{left:0;top:0;width:316px;height:190px;background:linear-gradient(135deg,#2a3f8a,#6a4ab0 55%,#1e4c6a)}
.feature-name{left:345px;top:12px;font-family:"Poppins",sans-serif;font-weight:700;font-size:14px;text-transform:uppercase}
.feature-rate{left:345px;top:34px;font-size:10px;font-weight:600;color:var(--yellow)}
.feature-text{left:345px;top:58px;width:250px;font-size:10.5px;line-height:1.5;color:var(--muted)}
.feature-list{left:625px;top:10px;width:180px;display:flex;flex-direction:column;gap:10px}
.feature-item{display:flex;align-items:center;gap:10px;height:38px;background:var(--panel-2);padding:0 8px;font-size:9px;font-weight:500}
.feature-item i{width:24px;height:24px;background:linear-gradient(135deg,#a0603a,#d6a050)}
.feature-tabs{left:0;top:190px;width:810px;height:30px;display:flex;border-top:1px solid var(--line)}
.feature-tabs span{flex:1;display:flex;align-items:center;justify-content:center;font-size:9px;font-weight:600;text-transform:uppercase;color:var(--muted);border-left:1px solid var(--line)}
.feature-tabs span:first-child{border-left:0;flex:0 0 316px}

/* Carousel */
.slide-side{top:1527px;height:311px}
.slide-left{left:0;width:262px;background:linear-gradient(135deg,#3a1a14,#a53a1a 50%,#2a1a20)}
.slide-right{left:936px;width:264px;background:linear-gradient(135deg,#0f3a3a,#1f6a5a 50%,#12202a)}
.slide-main{left:316px;top:1505px;width:570px;height:347px;background:linear-gradient(135deg,#6b6b6e,#4a7a6a 45%,#3d3d52)}
.slide-frame{left:310px;top:1499px}
.slide-label{left:316px;top:1878px;font-family:"Poppins",sans-serif;font-weight:700;font-size:12px;text-transform:uppercase}
.slide-meta{left:834px;top:1880px;font-size:9px;color:var(--muted);font-weight:600}
.slide-progress{left:316px;top:1918px;width:570px;height:3px;background:var(--line)}
.slide-progress i{position:absolute;left:70px;width:125px;height:3px;background:var(--green)}

/* Team */
.team-card{top:2193px;width:184px;height:232px;background:var(--panel);border:1px solid var(--line)}
.team-card .corner{position:absolute;top:0}
.team-photo{position:absolute;left:32px;top:22px;width:120px;height:120px;border-radius:50%;border:3px solid var(--white);background:radial-gradient(circle at 50% 40%,#9aa3ad,#3b4350)}
.team-name{position:absolute;left:0;top:178px;width:100%;text-align:center;font-family:"Poppins",sans-serif;font-weight:700;font-size:12px;text-transform:uppercase}
.team-role{position:absolute;left:0;top:198px;width:100%;text-align:center;font-size:9px;color:var(--green)}

/* Community */
.community{left:0;top:2506px;width:1200px;height:356px;background:
  radial-gradient(ellipse at 25% 50%,rgba(120,180,230,.35),transparent 45%),
  linear-gradient(135deg,#1f3f6a,#2a5a8a 45%,#163253)}
.community-shade{left:0;top:2506px;width:1200px;height:356px;background:linear-gradient(90deg,rgba(13,17,22,.2),rgba(13,17,22,.45) 50%,rgba(13,17,22,.2))}
.play{left:573px;top:2595px;width:54px;height:54px;border-radius:50%;background:var(--white);display:flex;align-items:center;justify-content:center}
.community-title{left:0;top:2655px;width:1200px;text-align:center;font-family:"Poppins",sans-serif;font-weight:800;font-size:36px;text-transform:uppercase}
.community-title em{font-style:normal;color:var(--green)}
.community-sub{left:0;top:2702px;width:1200px;text-align:center;font-size:11px;color:#d3dbe4}
.community-btn{left:525px;top:2732px;width:150px;height:40px;font-size:11px;background:rgba(13,17,22,.5)}

/* Roadmap */
.road-title{left:281px;top:2978px;font-family:"Poppins",sans-serif;font-weight:800;font-size:31px;line-height:1.08;text-transform:uppercase}
.road-text{left:281px;top:3100px;width:270px;font-size:11px;line-height:1.55;color:var(--muted)}
.road-btn{left:281px;top:3193px;width:122px;height:32px;font-size:10px;border-color:var(--yellow);background:transparent}
.road-art{left:262px;top:3247px;width:220px;height:124px;transform:skewY(-10deg);background:linear-gradient(135deg,#2b2c38,#8a5a2a 50%,#3a4a6a);border-radius:6px}
.road-line{left:604px;top:2972px;width:2px;height:552px;background:var(--line)}
.road-mark{left:598px;top:3050px}
.season{left:630px;width:310px;background:var(--panel);border:1px solid var(--line);padding:18px 20px}
.season h4{font-family:"Poppins",sans-serif;font-weight:700;font-size:13px;text-transform:uppercase;margin-bottom:14px}
.season li{list-style:none;display:flex;align-items:center;gap:8px;font-size:10px;color:var(--muted);margin-bottom:7px}
.season li i{width:7px;height:7px;background:var(--green)}
.season li.todo i{background:transparent}
.season-art{position:absolute;right:18px;top:22px;width:80px;height:120px;background:linear-gradient(180deg,#6a3a3a,#2a1e2a);border-radius:2px}

/* Trending */
.trend-title{left:193px;top:3706px;font-family:"Poppins",sans-serif;font-weight:800;font-size:17px;text-transform:uppercase;display:flex;align-items:center;gap:10px}
.trend-arrows{left:950px;top:3704px;display:flex;gap:10px}
.trend-arrows span{width:26px;height:26px;border-radius:50%;border:1px solid var(--muted-2);display:flex;align-items:center;justify-content:center}
.trend-card{top:3765px;width:262px;height:282px;background:var(--panel);border:1px solid var(--line);padding:14px}
.trend-head{display:flex;align-items:center;gap:8px}
.trend-head .dot-av{width:26px;height:26px}
.trend-user b{display:block;font-size:11px;font-weight:600}
.trend-user small{font-size:9px;color:var(--muted)}
.trend-art{margin-top:12px;width:232px;height:166px;background:radial-gradient(circle at 55% 50%,#5fd07a 0%,#3aa0a0 30%,#f0a040 60%,#f0a040 100%);border-radius:2px}
.trend-foot{display:flex;justify-content:space-between;align-items:flex-end;margin-top:12px}
.trend-foot small{display:block;font-size:9px;color:var(--muted)}
.trend-foot b{font-size:10px;color:var(--yellow);font-weight:600}
.trend-foot .yellow-btn{width:48px;height:20px}

/* Footer */
.footer-logo{left:193px;top:4142px;font-family:"Poppins",sans-serif;font-weight:800;font-size:24px;display:flex;align-items:center;gap:8px}
.footer-text{left:193px;top:4212px;width:280px;font-size:10.5px;line-height:1.55;color:var(--muted)}
.footer-contact{left:193px;top:4290px;font-size:10px;font-weight:600;color:var(--green);text-transform:uppercase}
.socials{left:193px;top:4320px;display:flex;gap:10px}
.socials i{width:20px;height:20px;border-radius:50%;background:var(--panel-2);border:1px solid var(--muted-2)}
.footer-col{top:4160px}
.footer-col h5{font-family:"Poppins",sans-serif;font-weight:700;font-size:12px;text-transform:uppercase;margin-bottom:14px}
.footer-col li{list-style:none;font-size:10px;color:var(--muted);margin-bottom:6px}
.footer-col p{font-size:10px;color:var(--muted);line-height:1.6;width:190px}
.news-input{margin-top:14px;width:190px;height:30px;border-bottom:1px solid var(--line);font-size:10px;color:var(--muted-2);display:flex;align-items:center}
.bottom-bar{left:0;top:4364px;width:1200px;height:40px;background:#080b0f;border-top:1px solid var(--line)}
.copyright{left:193px;top:14px;font-size:9px;color:var(--muted)}
.copyright em{font-style:normal;color:var(--green)}
.cards{left:815px;top:12px;display:flex;gap:6px}
.cards i{width:28px;height:17px;border-radius:2px;background:#e9edf2}
.cards i:nth-child(2){background:#ffbe18}
.cards i:nth-child(3){background:#2b6cd8}
.cards i:nth-child(5){background:#e6463a}
.to-top{left:1150px;top:4352px;width:28px;height:28px;background:var(--green);border-radius:3px;display:flex;align-items:center;justify-content:center}
</style>
</head>
<body>
<div class="canvas">

  <!-- Header & hero -->
  <section class="abs hero">
    <div class="abs hero-art" role="img" aria-label="Hero artwork of two fantasy game heroines in a glowing violet scene"></div>
    <div class="abs logo"><span class="logo-box"></span>Ravel</div>
    <nav class="abs nav"><span>Home</span><span>About us</span><span>Tournament</span><span>Pages</span><span>News</span><span>Contact</span></nav>
    <svg class="abs search" width="16" height="16" viewBox="0 0 16 16"><circle cx="7" cy="7" r="5" fill="none" stroke="#fff" stroke-width="2"/><line x1="11" y1="11" x2="15" y2="15" stroke="#fff" stroke-width="2"/></svg>
    <div class="abs hex-btn signin">Sign in</div>
    <svg class="abs menu" width="26" height="20" viewBox="0 0 26 20"><rect y="2" width="26" height="2" fill="#fff"/><rect x="8" y="9" width="18" height="2" fill="#fff"/><rect y="16" width="26" height="2" fill="#fff"/></svg>

    <div class="abs hero-kicker">Become the new</div>
    <h1 class="abs hero-title">Revolution</h1>
    <p class="abs hero-text">Build worlds, lead armies and shape every city in our next strategy sim, made by players for players who love deep play.</p>
    <div class="abs hex-btn hero-btn">Start now</div>
    <div class="abs hero-tabs"><span>Game guide</span><span>Features</span><span>Gameplay</span></div>
    <svg class="abs hero-edge" width="1200" height="50" viewBox="0 0 1200 50" preserveAspectRatio="none">
      <polygon points="0,10 600,28 1200,10 1200,50 0,50" fill="#0d1116"/>
      <polygon points="0,10 600,28 1200,10 1200,20 600,38 0,20" fill="#45f882"/>
    </svg>
  </section>

  <!-- NFT strip -->
  <section class="abs nft-strip">
    <div class="abs nft-card" style="left:193px">
      <div class="nft-thumb" role="img" aria-label="Cartoon creature collectible on yellow" style="background:linear-gradient(135deg,#f7c440,#e29a20)"></div>
      <div class="nft-info"><span class="nft-name">Wolf gaming art</span><span class="nft-by"><i class="dot-av"></i>Alex Rowe · Creator</span><span class="nft-foot">1.45 ETH <span class="yellow-btn">Buy</span></span></div>
    </div>
    <div class="abs nft-card" style="left:470px">
      <div class="nft-thumb" role="img" aria-label="Cartoon princess collectible on purple" style="background:linear-gradient(135deg,#8c6ad8,#5a3aa8)"></div>
      <div class="nft-info"><span class="nft-name">Forest princess</span><span class="nft-by"><i class="dot-av"></i>Mira Lane · Creator</span><span class="nft-foot">2.10 ETH <span class="yellow-btn">Buy</span></span></div>
    </div>
    <div class="abs nft-card" style="left:747px">
      <div class="nft-thumb" role="img" aria-label="Cartoon green creature collectible" style="background:linear-gradient(135deg,#5fd07a,#2a9a5a)"></div>
      <div class="nft-info"><span class="nft-name">Owl fireflies art</span><span class="nft-by"><i class="dot-av"></i>Tom Reid · Creator</span><span class="nft-foot">1.90 ETH <span class="yellow-btn">Buy</span></span></div>
    </div>
  </section>

  <!-- Top rated streamers -->
  <section class="abs streamers">
    <div class="abs eyebrow" style="left:0;top:92px;width:1200px">Know about us</div>
    <h2 class="abs sec-title" style="left:0;top:108px;width:1200px">Top rated steamers</h2>
    <div class="abs hex-btn tab-btn" style="left:490px">Buy hero</div>
    <div class="abs hex-btn tab-btn" style="left:610px;border-color:var(--yellow);background:transparent">Buy NFTs</div>
    <div class="abs avatars"><i class="avatar"></i><i class="avatar"></i><i class="avatar"></i><i class="avatar"></i><i class="avatar"></i><i class="avatar"></i></div>
    <div class="abs avatar-line"><i></i></div>

    <div class="abs feature">
      <div class="abs feature-art" role="img" aria-label="Game artwork of a hero warrior in a blue and violet battle scene"></div>
      <div class="abs feature-name">Human game</div>
      <div class="abs feature-rate">RATE 90%</div>
      <p class="abs feature-text">Lead a growing realm through seasons of war and trade. Plan each move, train your heroes and defend the walls before the next storm.</p>
      <div class="abs feature-list">
        <div class="feature-item"><i></i>Dragon Keeper Stuff</div>
        <div class="feature-item"><i></i>Sky Armor Set</div>
        <div class="feature-item"><i></i>Golden Staff</div>
      </div>
      <div class="abs feature-tabs"><span>Dragon soul</span><span>Art gallery</span><span>Support</span></div>
    </div>
  </section>

  <!-- Tournament carousel -->
  <div class="abs slide-side slide-left" role="img" aria-label="Game artwork of a fiery creature"></div>
  <div class="abs slide-side slide-right" role="img" aria-label="Game artwork of an armored warrior in green light"></div>
  <div class="abs slide-main" role="img" aria-label="Game artwork of an agile heroine in a tournament arena"></div>
  <svg class="abs slide-frame" width="582" height="359" viewBox="0 0 582 359">
    <path d="M0 30V0H30M552 0H582V30M582 329V359H552M30 359H0V329" fill="none" stroke="#45f882" stroke-width="3"/>
  </svg>
  <div class="abs slide-label">Squad Rush tournament</div>
  <div class="abs slide-meta">RATE 90%</div>
  <div class="abs slide-progress"><i></i></div>

  <!-- Team -->
  <div class="abs eyebrow" style="left:0;top:2090px;width:1200px">Our team member</div>
  <h2 class="abs sec-title" style="left:0;top:2106px;width:1200px">Active team members</h2>

  <div class="abs team-card" style="left:193px">
    <svg class="corner" width="184" height="60" viewBox="0 0 184 60"><polygon points="0,0 34,0 0,40" fill="#45f882"/><polygon points="184,0 150,0 184,40" fill="#45f882"/></svg>
    <div class="team-photo" role="img" aria-label="Team member portrait"></div>
    <div class="team-name">Killer Master</div><div class="team-role">Lead developer</div>
  </div>
  <div class="abs team-card" style="left:404px">
    <svg class="corner" width="184" height="60" viewBox="0 0 184 60"><polygon points="0,0 34,0 0,40" fill="#45f882"/><polygon points="184,0 150,0 184,40" fill="#45f882"/></svg>
    <div class="team-photo" role="img" aria-label="Team member portrait"></div>
    <div class="team-name">Tekhmark</div><div class="team-role">Designer</div>
  </div>
  <div class="abs team-card" style="left:612px">
    <svg class="corner" width="184" height="60" viewBox="0 0 184 60"><polygon points="0,0 34,0 0,40" fill="#45f882"/><polygon points="184,0 150,0 184,40" fill="#45f882"/></svg>
    <div class="team-photo" role="img" aria-label="Team member portrait"></div>
    <div class="team-name">Thompson Scot</div><div class="team-role">Producer</div>
  </div>
  <div class="abs team-card" style="left:822px">
    <svg class="corner" width="184" height="60" viewBox="0 0 184 60"><polygon points="0,0 34,0 0,40" fill="#45f882"/><polygon points="184,0 150,0 184,40" fill="#45f882"/></svg>
    <div class="team-photo" role="img" aria-label="Team member portrait"></div>
    <div class="team-name">Shakh Danial</div><div class="team-role">Game artist</div>
  </div>

  <!-- Community -->
  <div class="abs community" role="img" aria-label="Game artwork of a bearded wizard casting blue magic"></div>
  <div class="abs community-shade"></div>
  <div class="abs play"><svg width="18" height="20" viewBox="0 0 18 20"><polygon points="2,0 18,10 2,20" fill="#0d1116"/></svg></div>
  <h2 class="abs community-title">Join the <em>community</em></h2>
  <p class="abs community-sub">Join our Hubline server to chat with players and hear news first</p>
  <div class="abs hex-btn community-btn">Join Hubline</div>

  <!-- Roadmap -->
  <h2 class="abs road-title">A look into<br>roadmaps<br>seasons</h2>
  <p class="abs road-text">Follow each season of building, testing and launch as we shape our strategy sim, from first ideas to live game updates on every platform.</p>
  <div class="abs hex-btn road-btn">Roadmap</div>
  <div class="abs road-art" role="img" aria-label="Illustration of a phone showing a game board"></div>
  <div class="abs road-line"></div>
  <svg class="abs road-mark" width="20" height="24" viewBox="0 0 20 24"><rect x="5" y="0" width="3" height="24" fill="#45f882"/><polygon points="10,4 18,12 10,20" fill="#45f882"/></svg>

  <div class="abs season" style="top:2980px;height:171px">
    <h4>Season 1</h4>
    <ul><li><i></i>Battle Royale Mode</li><li><i></i>Ranked Modes</li><li><i></i>Closed Beta</li><li class="todo"><i></i>Core Content Building</li></ul>
    <div class="season-art" role="img" aria-label="Game character artwork"></div>
  </div>
  <div class="abs season" style="top:3165px;height:165px">
    <h4>Season 2</h4>
    <ul><li><i></i>Lore Creation &amp; Building</li><li><i></i>Mobile Apps Development</li><li class="todo"><i></i>Open Beta Test</li><li class="todo"><i></i>Full Launch Update</li></ul>
  </div>
  <div class="abs season" style="top:3344px;height:171px">
    <h4>Season 3</h4>
    <ul><li class="todo"><i></i>Switch to 3D gameplay</li><li class="todo"><i></i>Ranked Modes</li><li class="todo"><i></i>Closed Beta</li><li class="todo"><i></i>Building Content</li></ul>
  </div>

  <!-- Trending -->
  <div class="abs trend-title">Top trending <svg width="14" height="18" viewBox="0 0 14 18"><path d="M7 0C9 5 14 7 14 12A7 6 0 0 1 0 12C0 8 4 6 7 0Z" fill="#ff6a2a"/></svg></div>
  <div class="abs trend-arrows">
    <span><svg width="10" height="10" viewBox="0 0 10 10"><polyline points="7,1 3,5 7,9" fill="none" stroke="#8c96a3" stroke-width="1.5"/></svg></span>
    <span><svg width="10" height="10" viewBox="0 0 10 10"><polyline points="3,1 7,5 3,9" fill="none" stroke="#8c96a3" stroke-width="1.5"/></svg></span>
  </div>

  <div class="abs trend-card" style="left:193px">
    <div class="trend-head"><i class="dot-av"></i><div class="trend-user"><b>King Crypto</b><small>@kingcr</small></div></div>
    <div class="trend-art" role="img" aria-label="Collectible artwork of a colorful cartoon ape"></div>
    <div class="trend-foot"><div><small>Last bid</small><b>♦ 1.2032 ETH</b></div><span class="yellow-btn">Bid now</span></div>
  </div>
  <div class="abs trend-card" style="left:475px">
    <div class="trend-head"><i class="dot-av"></i><div class="trend-user"><b>Bidder Crypto</b><small>@bidder</small></div></div>
    <div class="trend-art" role="img" aria-label="Collectible artwork of a colorful cartoon ape"></div>
    <div class="trend-foot"><div><small>Last bid</small><b>♦ 1.2032 ETH</b></div><span class="yellow-btn">Bid now</span></div>
  </div>
  <div class="abs trend-card" style="left:757px;width:250px">
    <div class="trend-head"><i class="dot-av"></i><div class="trend-user"><b>Black Crypto</b><small>@blackc</small></div></div>
    <div class="trend-art" style="width:220px" role="img" aria-label="Collectible artwork of a colorful cartoon ape"></div>
    <div class="trend-foot"><div><small>Last bid</small><b>♦ 1.2032 ETH</b></div><span class="yellow-btn">Bid now</span></div>
  </div>

  <!-- Footer -->
  <div class="abs footer-logo"><span class="logo-box"></span>Ravel</div>
  <p class="abs footer-text">We build strategy and sim games for players who love to plan, trade and grow. Sign up to hear about each new launch and update.</p>
  <div class="abs footer-contact">Active with us</div>
  <div class="abs socials"><i></i><i></i><i></i><i></i></div>

  <div class="abs footer-col" style="left:504px"><h5>Quick link</h5><ul><li>Gaming</li><li>Product</li><li>All NFTs</li><li>Social Network</li><li>Domain Names</li><li>Collectibles</li></ul></div>
  <div class="abs footer-col" style="left:655px"><h5>Supports</h5><ul><li>Setting &amp; Privacy</li><li>Help &amp; Support</li><li>Live Auctions</li><li>Item Details</li><li>24/7 Support</li><li>Our News</li></ul></div>
  <div class="abs footer-col" style="left:809px"><h5>Newsletter</h5><p>Subscribe to our newsletter to get our latest game news.</p><div class="news-input">Your email</div></div>

  <div class="abs bottom-bar">
    <div class="abs copyright">Copyright © 2024 — All rights reserved by <em>Ravel</em></div>
    <div class="abs cards"><i></i><i></i><i></i><i></i><i></i></div>
  </div>
  <div class="abs to-top"><svg width="12" height="12" viewBox="0 0 12 12"><polyline points="2,8 6,4 10,8" fill="none" stroke="#0d1116" stroke-width="2"/></svg></div>

</div>
</body>
</html>
```